Stationary and envelopes

Need to have a new and edgy design for our stationary and matching envelopes. Check out our website at www.lorwinfieldservices.example

We do mainly construction and are the boots on the ground for the energy sector. I had you design our logo now next is stationary to make us stand out? ( boot print)

Target Market(s)

Corporate clients energy company

Font styles to use
Sans Serif

Requirements
Must have
• Logo and energy icons and what we do like the construction management and web address www.lorwinfieldservices.example
• Corporate office
• 48215 county road 62
• Brackett, CO 80744
• 555.274.6183 ( office)
Nice to have
• Logo energy,icons web address corporate office Sterling colorado
• Do not just cut and paste the logo on white paper
Should not have
• Kiddy look imature look

```html
<!DOCTYPE html>
<html lang="en">
<head>
<meta charset="utf-8">
<title>Lorwin Field Services — Stationery</title>
<link rel="stylesheet" href="https://fonts.googleapis.com/css2?family=Arimo:wght@400;700&display=swap">
<style>
:root{
  --bg:#d3d3d3;
  --navy:#0b1a3d;
  --brown:#5e1e0f;
  --brown-soft:#8a4a3a;
  --paper:#f0f0f0;
  --ink:#2a2a2a;
  --white:#ffffff;
}
*{box-sizing:border-box;margin:0;padding:0}
html,body{width:1200px;height:1041px;overflow:hidden}
body{background:var(--bg);font-family:"Arimo",Arial,sans-serif;color:var(--ink);position:relative}
.piece{position:absolute;background:var(--paper);box-shadow:0 1px 3px rgba(0,0,0,.18)}
.wordmark{font-weight:700;letter-spacing:.06em;line-height:1.05;text-transform:uppercase;display:flex;align-items:center;gap:5px;white-space:nowrap}
.wordmark .dot{display:inline-block;background:currentColor;flex:none}
.icon-strip{display:block;background:linear-gradient(90deg,var(--brown),var(--brown-soft),var(--brown));border-radius:2px;opacity:.85}

/* folder */
.folder{left:166px;top:76px;width:417px;height:541px;background:var(--navy);border-radius:3px;overflow:hidden}
.folder .spine{position:absolute;left:26px;top:0;bottom:0;width:3px;background:rgba(0,0,0,.22)}
.folder .wordmark{position:absolute;left:0;right:0;top:165px;justify-content:center;color:var(--white);font-size:19px}
.folder .wordmark .dot{width:12px;height:12px}
.folder .icon-band{position:absolute;left:0;right:0;top:434px;height:47px;background:var(--paper);display:flex;align-items:center;justify-content:center}
.folder .icon-strip{width:200px;height:22px}
.folder .web-band{position:absolute;left:0;right:0;top:481px;bottom:0;background:var(--brown);color:var(--white);font-size:7.5px;text-align:center;padding-top:23px}

/* letterhead */
.letter{left:615px;top:95px;width:403px;height:523px}
.letter .wordmark{position:absolute;left:30px;top:60px;color:var(--brown);font-size:9.5px}
.letter .wordmark .dot{width:7px;height:7px;background:var(--navy)}
.contact{position:absolute;font-size:4.6px;line-height:1.5;color:var(--ink);white-space:nowrap}
.letter .contact{left:276px;top:35px;border-left:1px solid var(--brown);padding-left:5px}
.contact .row{display:flex;align-items:center;gap:3px}
.contact svg{width:4px;height:4px;fill:var(--brown);flex:none}
.contact .gap{height:3px}
.letter .body{position:absolute;left:30px;top:137px;width:343px;font-size:5.1px;line-height:1.38;text-align:justify}
.letter .body p{margin-bottom:6px}
.letter .body .addr{margin-bottom:39px}
.letter .sign{display:flex;align-items:center;gap:16px;margin-top:10px}
.letter .sign .ink{width:58px;height:22px}
.services{position:absolute;font-size:4.4px;color:var(--navy);letter-spacing:.02em;text-transform:uppercase;display:flex;align-items:center;gap:3px;white-space:nowrap}
.letter .services{left:30px;top:496px}
.letter .icon-strip{position:absolute;right:30px;top:492px;width:80px;height:10px}
.stripe{position:absolute;left:0;right:0;bottom:0;height:8px}

/* envelopes */
.env-front{left:132px;top:645px;width:451px;height:196px}
.env-front .wordmark{position:absolute;left:24px;top:31px;color:var(--brown);font-size:8px}
.env-front .wordmark .dot{width:6px;height:6px;background:var(--navy)}
.env-front .services{left:24px;top:170px}
.env-front .icon-strip{position:absolute;right:30px;top:166px;width:80px;height:10px}
.env-back{left:615px;top:645px;width:451px;height:196px}
.env-back .flap{position:absolute;left:0;top:0;width:451px;height:66px}
.env-back .flap-name{position:absolute;left:0;right:0;top:27px;text-align:center;color:var(--white);font-size:13px;font-weight:700;letter-spacing:.1em}

/* business cards */
.card-front{left:417px;top:870px;width:167px;height:96px;overflow:hidden}
.card-front .name{position:absolute;left:13px;top:23px;font-size:5.3px;font-weight:700;color:var(--brown)}
.card-front .role{position:absolute;left:13px;top:30px;font-size:3.7px}
.card-front .wordmark{position:absolute;right:12px;top:20px;color:var(--brown);font-size:5.4px}
.card-front .wordmark .dot{width:4px;height:4px;background:var(--navy)}
.card-front .contact{left:13px;top:66px;font-size:3.4px}
.card-front .contact svg{width:3px;height:3px}
.card-front .post{position:absolute;right:12px;top:71px;font-size:3.4px;line-height:1.5;text-align:right}
.card-back{left:615px;top:870px;width:167px;height:96px;background:var(--navy);overflow:hidden}
.card-back .wordmark{position:absolute;left:0;right:0;top:28px;justify-content:center;color:var(--white);font-size:7.6px}
.card-back .wordmark .dot{width:5px;height:5px}
.card-back .icon-band{position:absolute;left:0;right:0;top:63px;height:23px;background:var(--paper);display:flex;align-items:center;justify-content:center}
.card-back .icon-strip{width:84px;height:11px}
.card-back .brown{position:absolute;left:0;right:0;bottom:0;height:10px;background:var(--brown)}
</style>
</head>
<body>

<svg width="0" height="0" style="position:absolute" aria-hidden="true">
  <defs>
    <symbol id="i-phone" viewBox="0 0 10 10"><path d="M2 0 4 2 3 4c1 1 2 2 3 3l2-1 2 2-2 2C4 10 0 6 0 2z"/></symbol>
    <symbol id="i-mail" viewBox="0 0 10 10"><path d="M0 2h10v6H0z"/></symbol>
    <symbol id="i-web" viewBox="0 0 10 10"><circle cx="5" cy="5" r="5"/></symbol>
  </defs>
</svg>

<!-- Presentation folder -->
<section class="piece folder">
  <div class="spine"></div>
  <div class="wordmark"><span class="dot"></span>Lorwin Field Services</div>
  <div class="icon-band">
    <span class="icon-strip" role="img" aria-label="Row of energy-sector service icons"></span>
  </div>
  <div class="web-band">www.lorwinfieldservices.example</div>
</section>

<!-- Letterhead -->
<section class="piece letter">
  <div class="wordmark"><span class="dot"></span>Lorwin Field Services</div>
  <div class="contact">
    <div>48215 County Rd 62</div>
    <div>Brackett, CO 80744</div>
    <div class="gap"></div>
    <div class="row"><svg><use href="#i-phone"/></svg>555.274.6183</div>
    <div class="row"><svg><use href="#i-mail"/></svg>info@lorwinfieldservices.example</div>
    <div class="row"><svg><use href="#i-web"/></svg>www.lorwinfieldservices.example</div>
  </div>
  <div class="body">
    <p style="margin-bottom:9px">30.09.2017</p>
    <p class="addr">Recipient's name<br>Lindenweg 14<br>10115 Berlin<br>Germany</p>
    <p style="margin-bottom:8px">Dear sir,</p>
    <p>Communication is a very integral part of living creatures, animals and humans. Communication may be verbal or written. Written communication however is only applicable to human beings. Can you even imagine a world without communication? Verbal communication can be through telephones, webcams or in person. Written communication is through letters, emails and mobile phone messages.</p>
    <p>In today's world of great inventions and technology, letters have somehow become redundant. It is the time for text messages or chats. But they still can communicate a lot more than all other modes of communication. Organizations and various government departments still bank on letters as a strong medium of communication. There is no comparison in costs of sending letters as compared to costs of mobile phone messages though – letters are far cheaper. Letters now commonly known as “hard copy documents” are considered more relevant and important than email copies of text messages as proof or evidence of some sort.</p>
    <p>Letters speak volumes about a person or an organization that writes it. So one must take utmost care ensuring that the language used in any letter is appropriate for the occasion for which it is being written. Since a letter is also a written proof or document, if there are certain things that should not form a part of it, then that too should be carefully handled.</p>
    <p>Writing a good letter is an art. But if for some reason someone is unable to write that perfect letter, these different types of letters provide a base for you to build on. Sample letters have been given for everyone to understand what all information needs to form a part of the letter type and then it can be customized.</p>
    <div class="sign">
      <div>Yours Sincerely,<br>Dana Morrow</div>
      <svg class="ink" viewBox="0 0 58 22" role="img" aria-label="Handwritten signature"><path d="M2 16C6 4 9 4 9 14c2-8 5-9 6-2 3-6 7-6 8 0 4-10 8-12 9-4 1 6-4 12-5 6 4-6 12-8 18-8M38 12l14-4" fill="none" stroke="#5b6fc4" stroke-width=".8"/></svg>
    </div>
  </div>
  <div class="services">Inspection <span>&gt;</span> Construction Management <span>&gt;</span> Temporary Workforce <span>&gt;</span> Land Services</div>
  <span class="icon-strip" role="img" aria-label="Row of energy-sector service icons"></span>
  <svg class="stripe" viewBox="0 0 403 8" preserveAspectRatio="none"><path d="M0 4h260l-4 4H0z" fill="var(--navy)"/><path d="M264 0h139v8H256z" fill="var(--brown)"/></svg>
</section>

<!-- Envelope front -->
<section class="piece env-front">
  <div class="wordmark"><span class="dot"></span>Lorwin Field Services</div>
  <div class="services">Inspection <span>&gt;</span> Construction Management <span>&gt;</span> Temporary Workforce <span>&gt;</span> Land Services</div>
  <span class="icon-strip" role="img" aria-label="Row of energy-sector service icons"></span>
  <svg class="stripe" viewBox="0 0 451 8" preserveAspectRatio="none"><path d="M0 4h312l-4 4H0z" fill="var(--navy)"/><path d="M316 0h135v8H308z" fill="var(--brown)"/></svg>
</section>

<!-- Envelope back -->
<section class="piece env-back">
  <svg class="flap" viewBox="0 0 451 66" preserveAspectRatio="none"><path d="M0 0h451l-12 60q-1 6-7 6H19q-6 0-7-6z" fill="var(--navy)"/></svg>
  <div class="flap-name">LORWIN</div>
</section>

<!-- Business card front -->
<section class="piece card-front">
  <div class="name">JORDAN PELL</div>
  <div class="role">General manager</div>
  <div class="wordmark"><span class="dot"></span>Lorwin Field Services</div>
  <div class="contact">
    <div class="row"><svg><use href="#i-phone"/></svg>555.274.6183</div>
    <div class="row"><svg><use href="#i-mail"/></svg>info@lorwinfieldservices.example</div>
    <div class="row"><svg><use href="#i-web"/></svg>www.lorwinfieldservices.example</div>
  </div>
  <div class="post">48215 Cy Rd 62<br>Brackett, CO 80744</div>
  <svg class="stripe" style="height:4px" viewBox="0 0 167 4" preserveAspectRatio="none"><path d="M0 2h100l-2 2H0z" fill="var(--navy)"/><path d="M102 0h65v4H98z" fill="var(--brown)"/></svg>
</section>

<!-- Business card back -->
<section class="piece card-back">
  <div class="wordmark"><span class="dot"></span>Lorwin Field Services</div>
  <div class="icon-band">
    <span class="icon-strip" role="img" aria-label="Row of energy-sector service icons"></span>
  </div>
  <div class="brown"></div>
</section>

</body>
</html>
```